Personal development products that change your life

This is a direct selling business that sells personal development courses, but also sells the business as well if desired. This is not MLM, and there is no handling of the product required, nor hassling friends or family. We are looking for business minded people wanting to work their own hours and achieve a desirable income from this. A success image or happy image on a flyer would be great. I'd like the website address to be displayed as well thanks. www.sunpath-growvista.com.au

Target Market(s)

Business-minded individuals searching for more finances. Self motivated, driven, interested in self development.

Industry/Entity Type

Business

Font styles to use
Sans Serif

Requirements
Must have
• Are you looking for
• - a franchise or business?
• - a change of career?
• - a back up income?
• Not MLM
• No product handling or shipping
• No hard sales required
• website: www.sunpath-growvista.com.au
Nice to have
• A picture or background of excited person jumping in the air, or some similar.
• Worded to enrol people interested in achieving more financial headway, or flexible hours, or travel and do this business from anywhere in the world.
• Only need access to a phone, internet connection and a desire to succeed.

```html
<!DOCTYPE html>
<html lang="en">
<head>
<meta charset="utf-8">
<title>Are you looking for – Sunpath Growvista flyer</title>
<link rel="stylesheet" href="https://fonts.googleapis.com/css2?family=Sacramento&family=Raleway:wght@400;500&display=swap">
<style>
  :root {
    --page-bg: #e6e6e6;
    --paper: #ffffff;
    --header-glow: rgba(255, 255, 255, 0.16);
    --sky-light: #7cc3ea;
    --headline-yellow: #e6e84a;
    --band-grey: #7b7891;
    --swoosh-green: #74c24a;
    --swoosh-blue: #38b3e6;
    --swoosh-pink: #ec9ac8;
    --swoosh-yellow: #f4ea1a;
    --body-grey: #7a7a7a;
    --link-blue: #5b7fd6;
    --white: #ffffff;
  }
  * { margin: 0; padding: 0; box-sizing: border-box; }
  html, body {
    width: 1200px;
    height: 960px;
    overflow: hidden;
    background: var(--page-bg);
  }
  .flyer {
    position: absolute;
    left: 280px;
    top: 30px;
    width: 640px;
    height: 900px;
    background: var(--paper);
    overflow: hidden;
    box-shadow: 0 2px 10px rgba(0, 0, 0, 0.12);
  }
  .flyer-art {
    position: absolute;
    inset: 0;
    width: 640px;
    height: 900px;
  }
  .headline-intro {
    position: absolute;
    left: 52px;
    top: 62px;
    font-family: "Sacramento", cursive;
    font-weight: 400;
    font-size: 56px;
    line-height: 0.85;
    color: var(--white);
    transform: rotate(-10deg);
    transform-origin: left top;
  }
  .headline-options {
    position: absolute;
    right: 40px;
    top: 40px;
    list-style: none;
    text-align: right;
    font-family: "Raleway", sans-serif;
    font-weight: 400;
    font-size: 23px;
    line-height: 1.15;
    color: var(--headline-yellow);
  }
  .band-text {
    font-family: "Raleway", sans-serif;
    font-size: 22px;
    fill: var(--white);
  }
  .pitch {
    position: absolute;
    left: 100px;
    right: 100px;
    top: 592px;
    text-align: center;
    font-family: "Raleway", sans-serif;
    font-weight: 500;
    font-size: 14.5px;
    line-height: 1.45;
    color: var(--body-grey);
  }
  .pitch p + p { margin-top: 16px; }
  .website {
    position: absolute;
    left: 0;
    right: 0;
    top: 842px;
    text-align: center;
    font-family: "Raleway", sans-serif;
    font-weight: 500;
    font-size: 16px;
    color: var(--link-blue);
  }
</style>
</head>
<body>
  <article class="flyer">
    <svg class="flyer-art" viewBox="0 0 640 900" xmlns="http://www.w3.org/2000/svg">
      <defs>
        <linearGradient id="photo-sky" x1="0" y1="0" x2="0" y2="1">
          <stop offset="0" stop-color="#1c47ad"/>
          <stop offset="0.55" stop-color="#2f6ccd"/>
          <stop offset="1" stop-color="#7aa9db"/>
        </linearGradient>
        <radialGradient id="photo-light" cx="0.55" cy="0.55" r="0.55">
          <stop offset="0" stop-color="#f2f2ee" stop-opacity="0.55"/>
          <stop offset="0.5" stop-color="#e9e6df" stop-opacity="0.2"/>
          <stop offset="1" stop-color="#ffffff" stop-opacity="0"/>
        </radialGradient>
        <linearGradient id="header-sky" x1="0" y1="0" x2="1" y2="1">
          <stop offset="0" stop-color="#4a6bc9"/>
          <stop offset="1" stop-color="#6aa6e0"/>
        </linearGradient>
        <path id="band-line" d="M0 597 Q330 535 640 444"/>
      </defs>

      <g class="hero-photo" role="img" aria-label="Photo of four happy people in white clothes jumping with arms raised against a clear blue sky above distant hills">
        <rect x="0" y="140" width="640" height="490" fill="url(#photo-sky)"/>
        <ellipse cx="330" cy="380" rx="300" ry="170" fill="url(#photo-light)"/>
        <path d="M0 548 Q110 520 230 540 Q300 550 360 532 L430 528 L430 630 L0 630 Z" fill="#3d4f66" opacity="0.7"/>
      </g>

      <g class="header-band">
        <path d="M0 0 H640 V150 Q330 175 0 205 Z" fill="url(#header-sky)"/>
        <circle cx="560" cy="55" r="160" fill="var(--header-glow)"/>
        <path d="M0 205 Q330 175 640 150" fill="none" stroke="var(--sky-light)" stroke-width="5"/>
        <path d="M0 211 Q330 181 640 156" fill="none" stroke="var(--white)" stroke-width="2" opacity="0.8"/>
      </g>

      <g class="colour-swoosh" fill="none">
        <path d="M0 566 Q180 508 420 474" stroke="var(--swoosh-green)" stroke-width="6"/>
        <path d="M0 556 Q220 494 480 456" stroke="var(--swoosh-blue)" stroke-width="5"/>
        <path d="M200 518 Q440 462 640 410" stroke="var(--sky-light)" stroke-width="4"/>
        <path d="M220 510 Q440 455 640 402" stroke="var(--swoosh-pink)" stroke-width="4"/>
        <path d="M240 502 Q450 446 640 393" stroke="var(--swoosh-yellow)" stroke-width="4"/>
      </g>

      <path class="benefit-band" d="M0 572 Q330 512 640 418 L640 468 Q330 558 0 622 Z" fill="var(--band-grey)"/>
      <path class="white-base" d="M0 622 Q330 558 640 468 V900 H0 Z" fill="var(--paper)"/>

      <g class="band-dividers" stroke="var(--white)" stroke-width="2">
        <line x1="150" y1="550" x2="153" y2="596"/>
        <line x1="382" y1="497" x2="388" y2="542"/>
      </g>
      <text class="band-text">
        <textPath href="#band-line" startOffset="30">Not MLM</textPath>
      </text>
      <text class="band-text">
        <textPath href="#band-line" startOffset="168">No product handling</textPath>
      </text>
      <text class="band-text">
        <textPath href="#band-line" startOffset="406">No hard sales required</textPath>
      </text>
    </svg>

    <h1 class="headline-intro">Are you<br>looking for</h1>
    <ul class="headline-options">
      <li>a franchise or business?</li>
      <li>a change of career?</li>
      <li>a back up income?</li>
    </ul>

    <section class="pitch">
      <p>We supply you<br>with the simple and complete<br>business model and all of your training<br>and support is only a phone call away.</p>
      <p>You provide the desire, motivation<br>and willingness to learn and have a real<br>passion for wanting a huge change,<br>personally and financially, in your life.</p>
      <p>Start the work / life balance<br>you've always wanted.</p>
    </section>

    <p class="website">www.sunpath-growvista.com.au</p>
  </article>
</body>
</html>
```